Graphic design for the use of marketing mainly in the form of promotional die cut stickers

I’m looking for a promotional design that incorporates business logo and phone number. My business is mobile mechanical repairs to earthmoving and mining equipment. Interests would also include images of services provided like earthmoving and mining equipment either reality or cartoon. Please don’t restrict yourself to the images provided as I’m always attracted to seeing the passion of the artist show through their work.
Updates

Phone number is 0four58142967

Target Market(s)

Similar people in the same industry

Industry/Entity Type

Mining, earthmoving, mechanical, diesel fitter

Requirements
Must have
• Business logo and phone number

```html
<!DOCTYPE html>
<html lang="en">
<head>
<meta charset="utf-8">
<title>Kestrel Diesel Pty Ltd – Promotional Sticker</title>
<link rel="stylesheet" href="https://fonts.googleapis.com/css2?family=Russo+One&family=Exo+2:ital,wght@1,800;1,900&display=swap">
<style>
  :root {
    --backdrop: #a3a3a3;
    --ink: #110e0f;
    --paper: #ffffff;
    --signal-red: #ea1016;
    --mark-red: #ff0500;
    --art-light: #f1f1f1;
    --art-mid: #c9c9c9;
  }
  html, body {
    margin: 0;
    padding: 0;
    width: 1200px;
    height: 960px;
    overflow: hidden;
    background: var(--backdrop);
  }
  .sticker {
    display: block;
    width: 1200px;
    height: 960px;
  }
  .brand-name {
    font-family: "Russo One", sans-serif;
    fill: var(--ink);
  }
  .service-line {
    font-family: "Exo 2", sans-serif;
    font-weight: 900;
    font-style: italic;
    fill: var(--paper);
  }
  .phone-number {
    font-family: "Exo 2", sans-serif;
    font-weight: 800;
    font-style: italic;
    fill: var(--paper);
  }
</style>
</head>
<body>
<svg class="sticker" viewBox="0 0 1200 960" xmlns="http://www.w3.org/2000/svg">
  <defs>
    <clipPath id="sticker-shape">
      <rect x="256" y="176" width="689" height="598" rx="12" ry="12"/>
    </clipPath>
    <linearGradient id="machinery-tone" x1="0" y1="0" x2="0" y2="1">
      <stop offset="0" stop-color="var(--art-light)"/>
      <stop offset="1" stop-color="var(--art-mid)"/>
    </linearGradient>
  </defs>

  <g class="sticker-body" clip-path="url(#sticker-shape)">
    <rect class="band-top" x="256" y="176" width="689" height="212" fill="var(--ink)"/>
    <rect class="band-logo" x="256" y="388" width="689" height="219" fill="var(--paper)"/>
    <rect class="band-service" x="256" y="607" width="689" height="66" fill="var(--ink)"/>
    <rect class="band-phone" x="256" y="673" width="689" height="101" fill="var(--signal-red)"/>
  </g>

  <rect class="machinery-illustration" x="303" y="189" width="599" height="234" rx="10"
        fill="url(#machinery-tone)" role="img"
        aria-label="Line illustration of a bulldozer and a mining haul truck"/>

  <g class="brand-lockup">
    <circle class="brand-dot" cx="361" cy="503" r="83" fill="var(--mark-red)"/>
    <text class="brand-name" x="468" y="513" font-size="90" textLength="453" lengthAdjust="spacingAndGlyphs">KESTREL</text>
    <text class="brand-name" x="460" y="559" font-size="45" textLength="448" lengthAdjust="spacingAndGlyphs">DIESEL PTY LTD</text>
  </g>

  <text class="service-line" x="284" y="656" font-size="44" textLength="633" lengthAdjust="spacingAndGlyphs">MECHANICAL REPAIRS</text>

  <text class="phone-number" x="284" y="749" font-size="72" textLength="632" lengthAdjust="spacingAndGlyphs">0four58 142 967</text>
</svg>
</body>
</html>
```